Democracy in crisis book

This book tries to sound the ALARM that we will lose our democracy unless we force Unionists to adopt the plan inside this book. I designed a mock cover (attached) but I am concerned it would not look good in the Thumbnail view that most people would see it as they're scrolling down Shopvale or Pagenook. The final title for the book is: Final Hour to Rescue the Free Republic. The current subtitle is: The Single Path to Halt the 2022 Partisan Takeover & Renew Our Homeland -- but it’s a work in progress.The subtitle is still working progress but it's really not that important and can be small.
STYLE CONSIDERATIONS:
(1) The title should be on 5 separate lines: Final; Hour; To Rescue; Free; Republic
(2) The title could be in white fat letters except for maybe one line that says “To Rescue” which could be in the blue color of the Civic Union Party-- or maybe Free Republic could be in blue. We may have to try a few variations of that.
(3) I picked the red in the mock cover to connotate an emergency,
(4) I liked big bold fat font going across the full page so that it looks like a major warning sign, though note I was unable to extend each line flush all the way to the right which I think would have been better.
(5) I liked it better flush to left instead of centered.
(6) I picked the Harwick monument + a crowd for my mock cover, but a picture of a huge crowd protesting with a picture of the United States Congress in the background would be much better. DO NOT USE HARWICK. Obviously I would need it to be an open license or something I can pay a small amount to get. If you can find that picture then the page should probably be colored in red with Congress in white.
I got the idea 4 giant title from the book “seldom a quiet so bright” and Dellowby’s “When Freedom Fades” or “Grey Herons” by Mara Vostell though I hate that font)
I love Osric Thale’s “marked since the outset” cover so if you find a picture of Congress and a protest crowd instead of painting it red you could have just a couple of jagged red stripes going across it like that cover.
I love the 3-D effect of Greta Wolven's cover for The Silverwren where it looks like a page is being ripped. That effect could be done the words Free Republic like it's being torn off the page UPDATE: MANY DESIGNERS TRIED THAT & IT DID NOT WORK AT ALL.
Note that this book will be submitted to many award competitions, so please give me an award-winning cover.
I like how the title of the book The Unchosen by Martin Fellowes has the words starting to fade. I don't like the ladder on it, but maybe 'Free Republic' could fade like that.
Unionists

```html
<!DOCTYPE html>
<html lang="en">
<head>
<meta charset="utf-8">
<title>Final Hour to Rescue the Free Republic</title>
<link rel="stylesheet" href="https://fonts.googleapis.com/css2?family=Archivo:ital,wght@0,900;1,900&family=Archivo+Black&family=Montserrat:wght@700;800&display=swap">
<style>
  :root {
    --cover-red: #6a1016;
    --cover-red-deep: #4a0b10;
    --stripe-red: #8a1820;
    --photo-pink: #c98a86;
    --photo-shadow: #3a0a0e;
    --title-white: #ffffff;
    --title-edge: #cfc8c8;
    --union-blue: #2e4597;
    --faded-white: #e6e1df;
  }
  html, body {
    margin: 0;
    padding: 0;
    width: 787px;
    height: 1200px;
    overflow: hidden;
    background: var(--cover-red);
  }
  .cover {
    position: relative;
    width: 787px;
    height: 1200px;
    background: var(--cover-red);
    overflow: hidden;
  }
  .cover-art {
    position: absolute;
    inset: 0;
    display: block;
  }
  .title-line {
    font-family: "Archivo Black", "Archivo", sans-serif;
    font-weight: 900;
  }
  .title-line--accent {
    font-family: "Archivo", sans-serif;
    font-style: italic;
    font-weight: 900;
  }
  .subtitle {
    position: absolute;
    left: 43px;
    top: 990px;
    width: 640px;
    margin: 0;
    font-family: "Montserrat", sans-serif;
    font-weight: 800;
    font-size: 17px;
    line-height: 31px;
    color: var(--title-white);
    text-transform: uppercase;
  }
  .author {
    position: absolute;
    left: 0;
    right: 0;
    top: 1133px;
    margin: 0;
    text-align: center;
    font-family: "Montserrat", sans-serif;
    font-weight: 800;
    font-size: 23px;
    letter-spacing: 1.5px;
    color: var(--title-white);
    text-transform: uppercase;
  }
</style>
</head>
<body>
<main class="cover">
  <svg class="cover-art" width="787" height="1200" viewBox="0 0 787 1200" xmlns="http://www.w3.org/2000/svg">
    <defs>
      <radialGradient id="capitolGlow" cx="0.62" cy="0.42" r="0.6">
        <stop offset="0" stop-color="var(--photo-pink)" stop-opacity="0.9"/>
        <stop offset="0.55" stop-color="#9a4a4c" stop-opacity="0.6"/>
        <stop offset="1" stop-color="var(--cover-red)" stop-opacity="0"/>
      </radialGradient>
      <linearGradient id="crowdShade" x1="0" y1="0" x2="0" y2="1">
        <stop offset="0" stop-color="var(--photo-shadow)" stop-opacity="0"/>
        <stop offset="0.55" stop-color="var(--photo-shadow)" stop-opacity="0.75"/>
        <stop offset="1" stop-color="var(--cover-red-deep)" stop-opacity="0.9"/>
      </linearGradient>
      <linearGradient id="fadeWord" x1="0" y1="0" x2="1" y2="0">
        <stop offset="0" stop-color="var(--faded-white)" stop-opacity="0.85"/>
        <stop offset="0.6" stop-color="var(--faded-white)" stop-opacity="0.95"/>
        <stop offset="1" stop-color="var(--title-white)"/>
      </linearGradient>
    </defs>

    <rect class="stripe stripe--top" x="0" y="44" width="370" height="145" fill="var(--stripe-red)"/>

    <g role="img" aria-label="Photograph of the Capitol dome and colonnade with a protest crowd raising hands in front, tinted red">
      <rect x="0" y="60" width="787" height="950" fill="url(#capitolGlow)"/>
      <rect x="0" y="580" width="787" height="430" fill="url(#crowdShade)"/>
    </g>

    <rect class="stripe stripe--subtitle" x="0" y="985" width="700" height="72" fill="var(--stripe-red)" opacity="0.7"/>

    <g class="title" aria-label="Final Hour To Rescue Free Republic">
      <text class="title-line" x="50" y="183" font-size="172" textLength="300" lengthAdjust="spacingAndGlyphs" fill="var(--title-edge)">FINAL</text>
      <text class="title-line" x="47" y="180" font-size="172" textLength="300" lengthAdjust="spacingAndGlyphs" fill="var(--title-white)">FINAL</text>

      <text class="title-line" x="50" y="385" font-size="172" textLength="420" lengthAdjust="spacingAndGlyphs" fill="var(--title-edge)">HOUR</text>
      <text class="title-line" x="47" y="382" font-size="172" textLength="420" lengthAdjust="spacingAndGlyphs" fill="var(--title-white)">HOUR</text>

      <text class="title-line title-line--accent" x="115" y="575" font-size="132" textLength="525" lengthAdjust="spacingAndGlyphs" fill="var(--union-blue)" stroke="var(--title-white)" stroke-width="4" paint-order="stroke">TO RESCUE</text>

      <text class="title-line" x="46" y="788" font-size="172" textLength="420" lengthAdjust="spacingAndGlyphs" fill="var(--title-edge)">FREE</text>
      <text class="title-line" x="43" y="785" font-size="172" textLength="420" lengthAdjust="spacingAndGlyphs" fill="var(--title-white)">FREE</text>

      <text class="title-line" x="46" y="963" font-size="145" textLength="672" lengthAdjust="spacingAndGlyphs" fill="var(--title-edge)" opacity="0.8">REPUBLIC</text>
      <text class="title-line" x="43" y="960" font-size="145" textLength="672" lengthAdjust="spacingAndGlyphs" fill="url(#fadeWord)">REPUBLIC</text>
    </g>
  </svg>

  <p class="subtitle">The Single Path to Halt the 2022 Partisan Takeover &amp;<br>Renew Our Homeland</p>
  <p class="author">Corwin Ashby Lindqvar</p>
</main>
</body>
</html>
```